Business Card

I need a business card for my work as an energy lawyer. I am a single prctioner and I consult to energy companies regarding a variety of legal issues involving environmental matters, energy efficiency, regulations and contractual arrangements. i need a distinctive business card that stands out and is easy to read. I like bold colors or high contrast. I like a sparse architectural design. The font should be easy to read (many of my clients use reading glasses and are concerned about small type). The card should communicate that I am somewhat different from ordinary legal counsel. Below are some examples of cards that I like. Thank you for your interest and thought. Glenn Dusty Harker
Updates

Thanks to everyone who has submitted a design.  My general comments are:

1.  I like the colourful cards and the high contrast cards.
2.  I prefer the use of icons for home address, phone, mobile and email.
3.  For the high contrast cards please use three colours - black background, and red and white for the logo or information.
4.  The mobile number area code should be 403 and not 404.
5.  I also need to add a direct phone line which is 403-517-6392.

Thank you,

Glenn Harker

Reason: I have briefly extended the deadline by three days to allow those individuals who responded early to revise their designs based upon the subsequent clarification of the colours (red, white, black background) and the request to use icons and add a direct phone number.

Industry/Entity Type

Business

```html
<!DOCTYPE html>
<html lang="en">
<head>
<meta charset="utf-8">
<title>Glenn Dusty Harker — Business Card</title>
<link href="https://fonts.googleapis.com/css2?family=Delius&family=Montserrat:wght@500;700&display=swap" rel="stylesheet">
<style>
  :root {
    --ink: #0b0b0b;
    --paper: #ffffff;
    --red: #e3132b;
    --rule: #8a8a8a;
    --backdrop: #ece9e4;
  }
  * { box-sizing: border-box; margin: 0; padding: 0; }
  html, body { width: 1200px; height: 800px; overflow: hidden; }
  body { background: var(--backdrop); position: relative; font-family: "Delius", cursive; }

  .card { position: absolute; width: 540px; height: 330px; overflow: hidden;
          box-shadow: 0 6px 18px rgba(0,0,0,.25); }
  .card-front { left: 112px; top: 45px; background: var(--paper); }
  .card-back { left: 500px; top: 435px; width: 525px; height: 308px; background: var(--ink); }

  .front-shape { position: absolute; inset: 0; }

  .brand { position: absolute; text-align: center; color: var(--red); font-family: "Delius", cursive; line-height: 1; }
  .brand-initials { display: block; font-size: 50px; letter-spacing: 2px; }
  .brand-name { display: block; font-size: 25px; margin-top: 4px; }
  .card-front .brand { left: 42px; top: 22px; }

  .website { position: absolute; font-family: "Montserrat", sans-serif; font-weight: 700; font-size: 11px; }
  .card-front .website { right: 36px; top: 52px; color: var(--ink); }

  .holder { position: absolute; left: 40px; top: 228px; width: 220px; text-align: center; }
  .holder-name { color: var(--paper); font-size: 18px; }
  .holder-title { color: var(--red); font-size: 12px; line-height: 1.5; margin-top: 8px; }

  .divider { position: absolute; left: 278px; top: 178px; width: 1px; height: 132px; background: var(--rule); }

  .contacts { position: absolute; left: 296px; top: 178px; list-style: none; color: var(--paper);
              font-family: "Montserrat", sans-serif; font-weight: 500; font-size: 12.5px; }
  .contacts li { display: flex; align-items: flex-start; gap: 22px; margin-bottom: 14px; }
  .contacts li:first-child { margin-bottom: 16px; }
  .contacts svg { width: 12px; height: 12px; flex: none; margin-top: 1px; fill: var(--paper); }
  .contacts .line-small { font-size: 11.5px; line-height: 1.45; }

  .back-band { position: absolute; left: 0; right: 0; top: 92px; height: 110px; background: var(--paper); }
  .card-back .brand { left: 0; right: 0; top: 98px; }
  .card-back .website { left: 0; right: 0; top: 222px; text-align: center; color: var(--paper); }
</style>
</head>
<body>

  <section class="card card-front" aria-label="Business card front">
    <svg class="front-shape" viewBox="0 0 540 330" preserveAspectRatio="none" aria-hidden="true">
      <path d="M0,190 Q250,118 540,98 L540,330 L0,330 Z" fill="var(--ink)"/>
      <path d="M0,238 Q210,150 500,104 Q240,168 0,256 Z" fill="var(--paper)"/>
    </svg>

    <div class="brand">
      <span class="brand-initials">GDH</span>
      <span class="brand-name">Glenn Dusty Harker</span>
    </div>
    <span class="website">www.dustyharker.com</span>

    <div class="holder">
      <p class="holder-name">Glenn Dusty Harker</p>
      <p class="holder-title">Barrister and Solicitor,<br>LLB, ICD.D</p>
    </div>

    <div class="divider"></div>

    <ul class="contacts">
      <li>
        <svg viewBox="0 0 12 12"><path d="M6 0a4 4 0 0 0-4 4c0 3 4 8 4 8s4-5 4-8a4 4 0 0 0-4-4zm0 5.6A1.6 1.6 0 1 1 6 2.4a1.6 1.6 0 0 1 0 3.2z"/></svg>
        <span class="line-small">2275 9th Avenue S.W.,<br>Calgary, Alberta</span>
      </li>
      <li>
        <svg viewBox="0 0 12 12"><rect x="3" y="0" width="6" height="12" rx="1"/><rect x="4" y="1.5" width="4" height="7.5" fill="var(--ink)"/></svg>
        <span>1.403.728.1945</span>
      </li>
      <li>
        <svg viewBox="0 0 12 12"><path d="M2.4 0.6l2 2.4-1.2 1.4c.7 1.6 2 2.9 3.6 3.6l1.4-1.2 2.4 2-1.3 2.4C4.6 11 1 7.4.8 2z"/></svg>
        <span>403-517-6392</span>
      </li>
      <li>
        <svg viewBox="0 0 12 12"><path d="M0 2h12v1L6 7 0 3z"/><path d="M0 4.4l6 4 6-4V10H0z"/></svg>
        <span>dusty@dustyharker.com</span>
      </li>
    </ul>
  </section>

  <section class="card card-back" aria-label="Business card back">
    <div class="back-band"></div>
    <div class="brand">
      <span class="brand-initials">GDH</span>
      <span class="brand-name">Glenn Dusty Harker</span>
    </div>
    <span class="website">www.dustyharker.com</span>
  </section>

</body>
</html>
```